Willow Cradle Pregnancy and Baby Massage

I need a web design for a new business, WILLOW CRADLE PREGNANCY AND BABY MASSAGE that I am in the process of setting up in the suburbs of Perth, Western Australia. The business is owned and operated by myself and my intention is to service Pregnant Mothers and Parents of Young Babies that would benefit from massage. I would like to have a "Home Page" and pages for "About Me", "Pregnancy Massage", "Baby Massage", a Pricing Page for Pregnancy Massage Sessions, a Pricing Page for Baby Massage Sessions, and a "Contact Me" page to allow clients to either contact me with queries or book available pregnancy massage sessions on a particular day of the week. I would also like a "News" page that would include articles I have written, news about new courses and a link to my Facebook page (yet to be set up). I would like to keep the colour schemes similar to my logo design colours. I need the design to be easy to follow and to appeal to a younger audience (20's to mid 30's).
The target audience is pregnant mothers-to-be wishing to receive massage treatments, and new parents and grandparents of small babies that would like to learn how to massage their babies.
The look and feel should be modern, professional, elegant and feminine.
I need the design to be in a standard format such that I can update the content by myself ( and does not need specialised software) as the company and business progresses.

Target Market(s)

Industry/Entity Type

Health And Wellness

Contact Information for Business Card

Card should have rounded edges. Design should have the same "feel" as the website. Contact Details of my business address, mobile phone, email and website should be included.

Coding

Coded - Design and coding required

Number of Pages Required

5+ page

Font styles to use
Script

Requirements
Must have
• Same colours as logo design. In cmyk system, the colours are: 20,60,0,0 which best result is pantone 681 and 40,40,0,0 which best result is pantone 2645. Card should include the logo design.

```html
<!DOCTYPE html>
<html lang="en">
<head>
<meta charset="utf-8">
<title>Baby Massage – Willow Cradle Pregnancy and Baby Massage</title>
<link href="https://fonts.googleapis.com/css2?family=Questrial&display=swap" rel="stylesheet">
<style>
  :root {
    --bar-dark: #3f3d45;
    --nav-text: #e4e2ea;
    --orchid: #a86aae;
    --lavender: #8778b6;
    --wave-purple: #b39bcb;
    --wave-lilac: #c9bfe0;
    --wave-pink: #e9c6da;
    --text: #3d3a40;
    --muted: #77737c;
    --footer-pink: #fbe4ec;
    --footer-plum: #4e4572;
    --footer-text: #e9e5f2;
    --white: #ffffff;
  }
  * { margin: 0; padding: 0; box-sizing: border-box; }
  html, body { width: 730px; height: 1200px; overflow: hidden; }
  body {
    position: relative;
    background: var(--white);
    font-family: "Questrial", "Helvetica Neue", Arial, sans-serif;
    color: var(--text);
  }

  .top-bar { position: absolute; left: 0; top: 0; width: 730px; height: 26px; background: var(--bar-dark); }
  .main-nav { position: absolute; right: 80px; top: 7px; display: flex; gap: 17px; font-size: 8px; }
  .main-nav a { color: var(--nav-text); text-decoration: none; }
  .main-nav a.current { color: var(--white); text-decoration: underline; }

  .header-wave { position: absolute; left: 0; top: 26px; width: 730px; height: 90px; }

  .brand-card {
    position: absolute; left: 80px; top: 0; width: 172px; height: 110px;
    background: var(--white); border-radius: 0 0 16px 16px;
    box-shadow: 0 3px 8px rgba(0,0,0,0.25);
  }
  .brand-card::after {
    content: ""; position: absolute; left: 6px; right: 6px; top: -2px; bottom: 6px;
    border: 1px dashed #77737c; border-radius: 0 0 12px 12px;
  }
  .brand-mark { position: absolute; left: 74px; top: 14px; width: 24px; height: 24px; border-radius: 50%; background: var(--orchid); }
  .brand-name {
    position: absolute; left: 14px; right: 14px; top: 46px; text-align: center;
    color: var(--orchid); font-size: 11px; line-height: 14px;
  }

  .photo-ring { position: absolute; left: 82px; top: 158px; width: 236px; height: 236px; border: 1px dashed #5c5960; border-radius: 50%; }
  .photo { position: absolute; left: 91px; top: 167px; width: 218px; height: 218px; border-radius: 50%;
    background: radial-gradient(circle at 45% 45%, #f4cdb8 0%, #e9b49a 55%, #f0efef 100%); }

  h1, h2 { font-weight: 400; }
  .about-title { position: absolute; left: 366px; top: 152px; font-size: 19px; color: var(--orchid); }
  .about-copy { position: absolute; left: 366px; top: 184px; width: 288px; font-size: 11.6px; line-height: 17.6px; }
  .about-copy p + p { margin-top: 4.5px; }

  .lesson-copy { position: absolute; left: 80px; top: 442px; width: 572px; font-size: 11.6px; line-height: 17.6px; }

  .quote { position: absolute; left: 80px; top: 526px; width: 572px; text-align: center; font-size: 11.6px; line-height: 17px; }
  .quote cite { display: block; margin-top: 2px; font-style: normal; font-size: 9px; color: var(--muted); }

  .benefits-title { position: absolute; left: 80px; top: 606px; font-size: 19px; color: var(--lavender); }
  .benefits-list { position: absolute; left: 80px; top: 639px; list-style: none; font-size: 11.5px; line-height: 21.45px; }
  .benefits-list li { padding-left: 12px; position: relative; }
  .benefits-list li::before { content: "›"; position: absolute; left: 0; top: -1px; font-size: 11px; color: var(--muted); }
  .source { position: absolute; left: 80px; top: 946px; font-size: 8px; }

  .footer-band { position: absolute; left: 0; top: 1005px; width: 730px; height: 127px;
    background: linear-gradient(100deg, #fdf0f4 0%, var(--footer-pink) 45%, #f9d9e4 100%); }
  .cert-badge { position: absolute; left: 86px; top: 1024px; width: 154px; height: 88px; border-radius: 8px; background: #ecd2e6; }
  .follow { position: absolute; left: 580px; top: 1045px; width: 70px; text-align: right; font-size: 9px; color: var(--text); }
  .social-dot { position: absolute; left: 609px; top: 1062px; width: 28px; height: 28px; border-radius: 50%; background: var(--footer-plum); }

  .site-footer { position: absolute; left: 0; top: 1132px; width: 730px; height: 68px; background: var(--footer-plum); color: var(--footer-text); text-align: center; font-size: 7.5px; }
  .footer-nav { margin-top: 20px; }
  .footer-nav a { color: var(--footer-text); text-decoration: none; }
  .footer-nav span { margin: 0 6px; }
  .copyright { margin-top: 9px; }
</style>
</head>
<body>
  <header>
    <div class="top-bar"></div>
    <svg class="header-wave" viewBox="0 0 730 90" preserveAspectRatio="none" aria-hidden="true">
      <rect width="730" height="90" fill="#ffffff"/>
      <path d="M0 0 H730 V78 C600 40 470 20 330 30 C200 40 90 70 0 80 Z" fill="var(--wave-pink)"/>
      <path d="M0 0 H730 V60 C640 20 520 0 400 8 C260 18 120 80 0 76 Z" fill="var(--wave-lilac)"/>
      <path d="M0 0 H730 V20 C620 10 520 4 430 8 C300 14 180 40 0 36 Z" fill="var(--wave-purple)"/>
    </svg>
    <nav class="main-nav">
      <a href="#">Home</a>
      <a href="#">About Me</a>
      <a href="#">Pregnancy Massage</a>
      <a href="#" class="current">Baby Massage</a>
      <a href="#">Pricing</a>
      <a href="#">News</a>
      <a href="#">Contact Me</a>
    </nav>
    <div class="brand-card">
      <div class="brand-mark"></div>
      <div class="brand-name">Willow Cradle<br>Pregnancy and Baby Massage</div>
    </div>
  </header>

  <main>
    <div class="photo-ring"></div>
    <div class="photo" role="img" aria-label="Photograph of adult hands gently cradling a baby's feet"></div>

    <h1 class="about-title">About Baby Massage</h1>
    <div class="about-copy">
      <p>Baby massage was first described in China circa 4000 years ago, then in India and Egypt, and was passed down from mother to daughter over the generations. It has become more popular in the Western world over the last 20 to 30 years.</p>
      <p>Massage can start from birth and is a wonderful way to soothe, calm and enjoy time with your baby, as well as helping with the bonding process.</p>
      <p>Long before babies are able to talk, they communicate with the new world around them through touch. Skin sensitivity is one of the earliest functions of the body. In fact, stimulation of the skin is essential for adequate organic and psychological development.</p>
    </div>

    <p class="lesson-copy">Whilst it is possible to learn the principles of baby massage from books, DVD’s, and social media, there is really no substitute for learning from an experienced and qualified instructor. During classes, you will be guided through the basic strokes ofBaby massage in a clear and relaxing manner. You will also learn to recognise and understand your baby’s cues, which is a very important part of baby massage.</p>

    <blockquote class="quote">
      “Being touched and caressed, being massaged, is food for the infant. Food as necessary&nbsp; as minerals,<br>vitamins, and proteins.”
      <cite>(Dr Henri Valcourt -&nbsp; Renowned Obstetrician and Author.)</cite>
    </blockquote>

    <h2 class="benefits-title">Benefits of Baby massage</h2>
    <ul class="benefits-list">
      <li>Relaxation of skeletal muscles</li>
      <li>Strengthens the immune system</li>
      <li>Reduces stress hormone levels in children and parents</li>
      <li>Improves sleep and regulates sleep patterns</li>
      <li>Relieves discomfort of wind, constipation, colic and reflux; sinus and chest congestion</li>
      <li>Reduces crying</li>
      <li>Enhances attachment and bonding</li>
      <li>Reduces symptoms of eczema</li>
      <li>Enhances emotions and improves mood</li>
      <li>Improves digestive, respiratory and circulatory system</li>
      <li>Reduces postnatal depression</li>
      <li>Reduces anxiety</li>
      <li>Increases blood and lymphatic circulation</li>
      <li>Enhances cognitive and motor development</li>
    </ul>
    <p class="source">Source: BTIS (Baby Touch Information Service)</p>
  </main>

  <div class="footer-band" role="img" aria-label="Soft pink background scattered with blurred hearts"></div>
  <div class="cert-badge" role="img" aria-label="Certification badge"></div>
  <p class="follow">Follow us on</p>
  <div class="social-dot" role="img" aria-label="Social page link"></div>

  <footer class="site-footer">
    <nav class="footer-nav">
      <a href="#">Home</a><span>|</span><a href="#">About Me</a><span>|</span><a href="#">Pregnancy Massage</a><span>|</span><a href="#">Baby Massage</a><span>|</span><a href="#">Pricing</a><span>|</span><a href="#">News</a><span>|</span><a href="#">Contact Me</a>
    </nav>
    <p class="copyright">Copyright &copy;&nbsp; 2017&nbsp; Willow Cradle Pregnancy &amp; Baby Massage.&nbsp;&nbsp; All rights reserved.</p>
  </footer>
</body>
</html>
```